Orbeo app design for cryptocurrency trading investment fund Vornexa

Vornexa is an investment fund that help investors with investing in cryptocurrencies such as Zentrix and Pallidor. We use our own trading platform to buy and sell crypto currencies on behalf of the investors. As an extra service we want to develop an Orbeo app for our investors. After logging in the Orbeo app they can get a real-time insight in the value of their portfolio. We have created wireframes of these pages in attached zip file. This zip file also contains the logo of Vornexa.

We need you to design a clean professional and fresh app design based on the wireframes. The app design should contain the corporate identity of Vornexa and thus the following color codes and font type must be used:

Color 1: 489e95
Color 2: 474646
Font type: Open Sans

login.png
The investor first has to login the app

home.png
The first page the investor sees after logging in.

account.png
In the account section the investor can change his login access details to the app

account_b.png
On this page he can change his password.

Coin page (added as separate file)
This is the page that shows up when you click on one of the coins.

Target Market(s)

Investors who invest the minimum amount of € 100.000

Industry/Entity Type

Tech

Requirements
Must have
• Professional modern design
Should not have
• cheap colourful creative look and feel.

```html
<!DOCTYPE html>
<html lang="en">
<head>
<meta charset="utf-8">
<title>Vornexa – Orbeo app design</title>
<link rel="stylesheet" href="https://fonts.googleapis.com/css2?family=Open+Sans:wght@300;400;600;700&display=swap">
<style>
  :root{
    --teal:#489e95;
    --teal-dark:#3c857d;
    --ink:#474646;
    --screen:#1b1f1e;
    --screen-row:#222a28;
    --line:#2f5a55;
    --label:#5f7f7a;
    --text-soft:#8fa9a5;
    --white:#ffffff;
    --bg-deep:#28414f;
    --bg-mid:#2f4a58;
  }
  *{box-sizing:border-box;margin:0;padding:0}
  html,body{width:1200px;height:1014px;overflow:hidden}
  body{
    font-family:"Open Sans",sans-serif;
    background:
      radial-gradient(ellipse 620px 420px at 360px 40px, rgba(225,236,214,.85), rgba(150,175,170,.35) 45%, rgba(40,65,79,0) 80%),
      linear-gradient(180deg,var(--bg-mid),var(--bg-deep));
    position:relative;
    color:var(--white);
  }

  /* brand block */
  .brand-name{
    position:absolute;left:700px;top:66px;width:416px;
    font-size:112px;font-weight:300;letter-spacing:-2px;line-height:1;
    color:var(--white);text-align:right;
  }
  .brand-intro{
    position:absolute;right:85px;top:244px;width:420px;
    text-align:right;font-size:10.4px;font-weight:600;letter-spacing:.5px;
    line-height:32.8px;color:var(--white);
  }

  /* screens */
  .screen{
    position:absolute;top:594px;width:198px;height:358px;
    background:var(--screen);border-radius:12px;overflow:hidden;
    box-shadow:0 8px 20px rgba(0,0,0,.25);
  }
  .screen--login{left:46px}
  .screen--password{left:276px}
  .screen--home{left:502px;width:200px}
  .screen--coin{left:732px;width:200px}
  .screen--account{left:962px;width:200px}
  .abs{position:absolute}

  .app-header{position:absolute;left:0;right:0;top:14px;height:24px}
  .app-header .wordmark{position:absolute;left:16px;top:4px;font-size:12px;font-weight:600;color:var(--teal)}
  .app-header .nav-icon{position:absolute;top:4px;width:14px;height:14px}

  .welcome{right:25px;top:56px;font-size:10px;font-weight:700;color:var(--teal);letter-spacing:.6px}
  .login-mark{left:26px;top:68px;font-size:28px;font-weight:400;color:var(--teal);letter-spacing:.5px}

  .field-label{font-size:6px;color:var(--label);letter-spacing:.3px;text-transform:uppercase}
  .field-line{height:1px;background:var(--line)}

  .check{left:56px;top:235px;display:flex;align-items:center;gap:7px;font-size:10px;color:var(--teal)}
  .btn{
    background:var(--teal);color:var(--white);border-radius:14px;
    font-size:12px;font-weight:700;text-align:center;line-height:26px;
  }
  .forgot{left:0;right:0;top:318px;text-align:center;font-size:9.5px;color:var(--teal)}

  /* value cards */
  .card{
    position:absolute;top:62px;width:51px;height:36px;border-radius:7px;
    background:var(--teal-dark);color:#142220;text-align:center;
    font-size:7.2px;font-weight:600;padding-top:6px;line-height:15px;
  }
  .card--active{background:var(--teal);box-shadow:0 0 7px rgba(72,158,149,.6)}
  .card-label{position:absolute;top:107px;width:64px;text-align:center;font-size:4.4px;color:var(--label);letter-spacing:.2px}

  .coin-dots{left:0;right:0;top:134px;height:14px}
  .coin-dot{position:absolute;top:0;width:13px;height:13px;border:1.5px solid #4a5654;border-radius:50%}

  .coin-table{left:0;top:153px;width:200px;border-collapse:collapse;font-size:5.3px;color:var(--text-soft)}
  .coin-table th{font-weight:700;color:var(--text-soft);height:13px;text-align:center}
  .coin-table td{height:17.5px;text-align:center}
  .coin-table th:first-child,.coin-table td:first-child{text-align:left;padding-left:11px;width:36px}
  .coin-table tr:nth-child(even) td{background:var(--screen-row)}

  .band{left:0;right:0;top:236px;height:18px;background:var(--teal);color:var(--white);font-size:6.5px;font-weight:700;letter-spacing:.4px;padding:5px 10px}

  .periods{display:flex;gap:5px;left:11px}
  .period{width:21.5px;height:12px;border-radius:2px;background:var(--teal-dark);color:#142220;font-size:5.6px;font-weight:700;text-align:center;line-height:12px}
  .period--on{background:var(--white);color:#142220}

  .fab{width:20px;height:20px;border-radius:50%;background:var(--teal)}

  .photo-area{left:0;top:0;width:200px;height:172px;
    background:linear-gradient(180deg,#0d1420 0%,#1d2a3c 45%,#7e93a8 70%,#2c3d52 82%,#131b26 100%)}
  .account-value{font-size:12.5px;font-weight:300;color:var(--teal)}
  .chev{font-size:10px;color:var(--white)}
</style>
</head>
<body>

  <div class="brand-name">Vornexa</div>
  <p class="brand-intro">Vornexa is an investment fund that help investors with investing<br>in cryptocurrencies such as Zentrix and Pallidor. We use our<br>own trading platform to buy and sell crypto currencies on behalf<br>of the investors. As an extra service we want to develop an<br>Orbeo app for our investors.</p>

  <svg width="0" height="0" style="position:absolute">
    <defs>
      <symbol id="icon-user" viewBox="0 0 14 14"><circle cx="7" cy="7" r="6" fill="none" stroke="#489e95" stroke-width="1.1"/><circle cx="7" cy="5.5" r="2.2" fill="none" stroke="#489e95" stroke-width="1.1"/><path d="M3.5 11.3c.8-1.9 2-2.8 3.5-2.8s2.7.9 3.5 2.8" fill="none" stroke="#489e95" stroke-width="1.1"/></symbol>
      <symbol id="icon-chart" viewBox="0 0 14 14"><polyline points="1,13 5,7 8,9 13,1" fill="none" stroke="#489e95" stroke-width="1.2"/><circle cx="5" cy="7" r="1" fill="#489e95"/><circle cx="8" cy="9" r="1" fill="#489e95"/><circle cx="13" cy="1.5" r="1" fill="#489e95"/></symbol>
      <symbol id="icon-mail" viewBox="0 0 14 14"><rect x="1" y="3" width="12" height="8.5" fill="none" stroke="#489e95" stroke-width="1.1"/><polyline points="1,3 7,8 13,3" fill="none" stroke="#489e95" stroke-width="1.1"/></symbol>
      <symbol id="icon-down" viewBox="0 0 20 20"><path d="M10 5v9M6.5 10.5 10 14l3.5-3.5" fill="none" stroke="#fff" stroke-width="1.6"/></symbol>
    </defs>
  </svg>

  <!-- Login -->
  <section class="screen screen--login">
    <div class="abs welcome">Welcome to the</div>
    <div class="abs login-mark">Vornexa</div>
    <div class="abs field-label" style="left:17px;top:138px">Username</div>
    <div class="abs field-line" style="left:17px;right:17px;top:174px"></div>
    <div class="abs field-label" style="left:17px;top:184px">Password</div>
    <div class="abs field-line" style="left:17px;right:17px;top:220px"></div>
    <div class="abs check"><svg width="12" height="12" viewBox="0 0 12 12"><rect x=".5" y="1.5" width="10" height="10" fill="none" stroke="#489e95"/><path d="M3 6l2.5 2.5L11 1.5" fill="none" stroke="#489e95" stroke-width="1.3"/></svg>Stay logged in</div>
    <div class="abs btn" style="left:17px;width:164px;top:266px">Log in</div>
    <div class="abs forgot">Forgot password ?</div>
  </section>

  <!-- Change password -->
  <section class="screen screen--password">
    <header class="app-header">
      <span class="wordmark">Vornexa</span>
      <svg class="nav-icon" style="left:100px"><use href="#icon-user"/></svg>
      <svg class="nav-icon" style="left:137px"><use href="#icon-chart"/></svg>
      <svg class="nav-icon" style="left:174px"><use href="#icon-mail"/></svg>
    </header>
    <div class="abs field-label" style="left:17px;top:129px">Old password</div>
    <div class="abs field-line" style="left:17px;right:17px;top:164px"></div>
    <div class="abs field-label" style="left:17px;top:175px">New password</div>
    <div class="abs field-line" style="left:17px;right:17px;top:211px"></div>
    <div class="abs field-label" style="left:17px;top:222px">Confirm password</div>
    <div class="abs field-line" style="left:17px;right:17px;top:258px"></div>
    <div class="abs btn" style="left:17px;width:164px;top:286px">Save</div>
  </section>

  <!-- Home -->
  <section class="screen screen--home">
    <header class="app-header">
      <span class="wordmark">Vornexa</span>
      <svg class="nav-icon" style="left:101px"><use href="#icon-user"/></svg>
      <svg class="nav-icon" style="left:138px"><use href="#icon-chart"/></svg>
      <svg class="nav-icon" style="left:175px"><use href="#icon-mail"/></svg>
    </header>
    <div class="card card--active" style="left:10px">€100,000.00<br>100%</div>
    <div class="card" style="left:75px">€110,000.00<br>110%</div>
    <div class="card" style="left:140px">€10,000.00<br>10%</div>
    <div class="card-label" style="left:4px">INVESTED AMOUNT</div>
    <div class="card-label" style="left:69px">CURRENT BALANCE</div>
    <div class="card-label" style="left:133px">PROFIT/LOSS</div>
    <div class="abs coin-dots">
      <span class="coin-dot" style="left:60px"></span><span class="coin-dot" style="left:90px"></span><span class="coin-dot" style="left:119px"></span><span class="coin-dot" style="left:148px"></span><span class="coin-dot" style="left:177px"></span>
    </div>
    <table class="abs coin-table">
      <tr><th>COIN</th><th>PLD/EUR</th><th>KVR</th><th>LMT</th><th>ZTX</th><th>QRN</th></tr>
      <tr><td>CHANGE</td><td>+ 9.4%</td><td>- 15.11%</td><td>+ 4.4%</td><td>+ 1.6%</td><td>+ 9.24%</td></tr>
      <tr><td>PRICE (€)</td><td>295,22</td><td>45,89</td><td>235,56</td><td>2.400,50</td><td>2,03</td></tr>
      <tr><td>HOLDINGS</td><td>2.552</td><td>132.009</td><td>38.236</td><td>59.60</td><td>4.952</td></tr>
      <tr><td>H (€)</td><td>755.87K</td><td>556.72K</td><td>255.40K</td><td>143.36K</td><td>10.044</td></tr>
    </table>
    <div class="abs band">PORTFOLIO CHART</div>
    <div class="abs periods" style="top:267px">
      <span class="period">1D</span><span class="period">7D</span><span class="period">1M</span><span class="period period--on">3M</span><span class="period">6M</span><span class="period">1Y</span><span class="period">ALL</span>
    </div>
    <svg class="abs fab" style="left:170px;top:292px"><circle cx="10" cy="10" r="10" fill="#489e95"/><use href="#icon-down"/></svg>
    <svg class="abs" role="img" aria-label="Portfolio value line chart" style="left:0;top:294px" width="200" height="64" viewBox="0 0 200 64">
      <g font-size="4" fill="#8fa9a5" font-family="Open Sans,sans-serif"><text x="6" y="7">400</text><text x="6" y="23">350</text><text x="6" y="39">300</text><text x="6" y="55">250</text></g>
      <polyline fill="none" stroke="#489e95" stroke-width="1" points="20,64 26,56 30,62 36,48 40,58 46,44 50,54 54,46 58,52 62,42 66,50 72,30 78,48 84,34 88,50 94,36 98,52 104,38 108,46 114,40 118,50 124,42 128,48 134,40 140,52 146,36 154,24 160,36 166,46 170,58 176,46"/>
    </svg>
  </section>

  <!-- Coin detail -->
  <section class="screen screen--coin">
    <header class="app-header">
      <span class="wordmark">Vornexa</span>
      <svg class="nav-icon" style="left:101px"><use href="#icon-user"/></svg>
      <svg class="nav-icon" style="left:138px"><use href="#icon-chart"/></svg>
      <svg class="nav-icon" style="left:175px"><use href="#icon-mail"/></svg>
    </header>
    <div class="card card--active" style="left:10px">€45.000<br>45%</div>
    <div class="card" style="left:75px">€49.500<br>- 10%</div>
    <div class="card" style="left:140px">€4.500<br>10%</div>
    <div class="card-label" style="left:4px">INVESTED AMOUNT</div>
    <div class="card-label" style="left:69px">CURRENT BALANCE</div>
    <div class="card-label" style="left:133px">PROFIT/LOSS</div>
    <div class="abs periods" style="top:140px">
      <span class="period">1D</span><span class="period">7D</span><span class="period">1M</span><span class="period period--on">3M</span><span class="period">6M</span><span class="period">1Y</span><span class="period">ALL</span>
    </div>
    <svg class="abs fab" style="left:170px;top:165px"><circle cx="10" cy="10" r="10" fill="#489e95"/><use href="#icon-down"/></svg>
    <svg class="abs" role="img" aria-label="Coin price line chart, April to June" style="left:0;top:170px" width="200" height="160" viewBox="0 0 200 160">
      <g font-size="4" fill="#8fa9a5" font-family="Open Sans,sans-serif">
        <text x="6" y="10">400</text><text x="6" y="26">350</text><text x="6" y="42">300</text><text x="6" y="58">250</text><text x="6" y="74">200</text><text x="6" y="90">150</text><text x="6" y="106">100</text><text x="6" y="122">50</text><text x="11" y="138">0</text>
        <text x="38" y="150">APR</text><text x="100" y="150">MAY</text><text x="162" y="150">JUN</text>
      </g>
      <polyline fill="none" stroke="#489e95" stroke-width="1" points="20,116 24,108 28,118 32,104 36,116 40,100 44,112 48,98 52,110 56,102 60,108 64,96 68,106 72,88 76,100 80,108 86,84 90,96 96,72 100,86 104,68 110,78 114,56 118,66 122,50 126,60 130,42 134,62 138,30 142,50 146,40 150,28 156,48 162,66 168,58"/>
    </svg>
  </section>

  <!-- Account -->
  <section class="screen screen--account">
    <div class="abs photo-area" role="img" aria-label="Night sky over calm water with a hot air balloon"></div>
    <header class="app-header">
      <span class="wordmark">Vornexa</span>
      <svg class="nav-icon" style="left:101px"><use href="#icon-user"/></svg>
      <svg class="nav-icon" style="left:138px"><use href="#icon-chart"/></svg>
      <svg class="nav-icon" style="left:175px"><use href="#icon-mail"/></svg>
    </header>
    <div class="abs field-label" style="left:18px;top:204px;color:#a9b6b4">Email address</div>
    <div class="abs account-value" style="left:18px;top:216px">marten@vornexa.com</div>
    <div class="abs chev" style="left:175px;top:218px">›</div>
    <div class="abs field-label" style="left:18px;top:250px;color:#a9b6b4">Password</div>
    <div class="abs account-value" style="left:18px;top:262px">change password</div>
    <div class="abs chev" style="left:175px;top:264px">›</div>
  </section>

</body>
</html>
```